PPT Template for a company that develops software and intellectual property for use by accountants a

We are a boutique firm that develops specialised reporting applications, financial and non-financial reporting content, checklists and other intellectual property for use by business consultants and accounting firms in particular. The applications and content we are creating is strategically focussed and we are required to produce reports and presentations and our current templates are simply not sufficient.

Excel worksheets, graphs and other graphics are regularly embedded into the presentations
We have our logo in 4 colour palettes and will require the winning version to be provided in all 4 colours plus B&W. There is one single logo but the name “Harbor Ledger Pathfinders” is presented in 3 different styles for use depending on the space available etc.
Our clients will typically take our products and rebrand/co brand these (we require them to at least say that there product is “powered by Harbor Ledger Pathfinders” with the logo.
The templates you provide will be used to create marketing presentations, proposal presentations and our standard documents that clients will rebrand or cobrand under license.

A Powerpoint Document Slide Template

Cover page layout, back page, intermediate page heading, in colours and styles based on the logo, title styles, and an intermediate or chapter heading slide style. Many of our presentations contain slides with tables, diagrams, flowcharts and text, including simple lists of bullet points. As above, you will see in our style guide that we have four coloured logos – we would like one version in each. We recommend that we finalise the design using the maroon version and then this be used as the base for the other colour palettes.
Again, the cover should be bold and draw attention but remain professional.

We are looking for something that works in both 4:3 and 16:9 (or two templates please)

We like a clear professional and simple look.

Deliverable: PowerPoint template file (.potx extension) for PowerPoint 2007 with at least a “cover” layout, a “title and content” layout, and a simplified slide layout, as well as “back cover”. Please embed any fonts used.

Industry/Entity Type

Financial

```html
<!DOCTYPE html>
<html lang="en">
<head>
<meta charset="utf-8">
<title>Harbor Ledger Pathfinders – Slide Template Overview</title>
<link href="https://fonts.googleapis.com/css2?family=Open+Sans:wght@300;400;600;700&family=Oswald:wght@500;600&display=swap" rel="stylesheet">
<style>
  :root{
    --stage:#a9a9a9;
    --paper:#ffffff;
    --orange:#f57b14;
    --charcoal:#4a4a4a;
    --ink:#333333;
    --muted:#7a7a7a;
    --rule:#c4c4c4;
    --slate:#808080;
    --pie-blue:#4f81bd;
    --pie-red:#c0504d;
    --pie-green:#9bbb59;
    --bar-cyan:#4bacc6;
  }
  *{box-sizing:border-box;margin:0;padding:0}
  html,body{width:1200px;height:700px;overflow:hidden;background:var(--stage)}
  body{position:relative;font-family:"Open Sans",Arial,sans-serif;color:var(--ink)}
  .slide{position:absolute;width:280px;height:210px;background:var(--paper);overflow:hidden}
  .slide-title{position:absolute;left:10px;top:18px;font-size:10px;font-weight:600;color:var(--ink)}
  .header-rule{position:absolute;left:10px;right:10px;top:33px;height:1px;background:var(--rule)}
  .brand-dot{position:absolute;right:40px;top:6px;width:15px;height:15px;border-radius:50%;background:var(--orange)}
  .brand-name{position:absolute;right:10px;top:25px;font-size:5.3px;color:var(--charcoal)}
  .wave{position:absolute;left:0;bottom:0;width:280px;height:60px}
  .footer-name{position:absolute;left:10px;bottom:6px;font-size:5.6px;font-weight:700;color:#fff;line-height:1.25}
  .page-no{position:absolute;right:9px;bottom:7px;width:10px;height:10px;border-radius:50%;background:#fff;color:var(--orange);font-size:5.5px;font-weight:700;text-align:center;line-height:10px}
  .body-copy{font-size:4.6px;line-height:1.55;color:var(--muted);text-align:justify}
  .placeholder{position:absolute}

  /* cover */
  .cover-art,.closing-art{position:absolute;left:0;top:0;width:280px;height:210px}
  .cover-mark{position:absolute;left:123px;top:26px;width:34px;height:34px;border-radius:50%;background:var(--orange)}
  .cover-name{position:absolute;left:0;right:0;top:76px;text-align:center;font-size:9px;color:var(--charcoal)}
  .cover-title{position:absolute;left:0;right:0;top:148px;text-align:center;font-family:"Oswald",Impact,sans-serif;font-weight:600;font-size:13.5px;color:#fff;letter-spacing:.3px}
  .cover-title::before,.cover-title::after{content:"";position:absolute;top:10px;width:52px;height:1px;background:#fff}
  .cover-title::before{left:6px}.cover-title::after{right:6px}
  .cover-sub{position:absolute;left:0;right:0;top:168px;text-align:center;font-family:"Oswald",Impact,sans-serif;font-weight:500;font-size:5px;color:#fff}

  /* contents */
  .toc-item{position:absolute;display:flex;align-items:center;gap:8px;font-size:6.4px;color:var(--muted)}
  .toc-num{width:11px;height:11px;border-radius:50%;background:var(--orange);color:#fff;font-size:5.5px;text-align:center;line-height:11px}

  /* planning */
  .step-label{position:absolute;top:48px;color:#fff;text-align:center;line-height:1.1;width:70px}
  .step-label small{display:block;font-size:5.5px}
  .step-label span{font-size:9px}

  /* team */
  .portrait{position:absolute;top:45px;width:48px;height:48px;border-radius:50%;border:1.5px solid var(--orange);background:#fff;padding:3px}
  .portrait div{width:100%;height:100%;border-radius:50%;background:radial-gradient(circle at 50% 40%,#d9d2cc,#6f6a66)}
  .team-copy{position:absolute;top:100px;width:62px;font-size:4.6px;line-height:1.55;color:var(--muted);text-align:center}

  .callout{position:absolute;background:var(--orange);color:#fff;font-size:4.6px;line-height:1.55;padding:8px;text-align:justify}
  .chart-label{position:absolute;font-size:6.3px;color:var(--ink)}

  .highlight-grid{position:absolute;left:12px;top:45px;display:grid;grid-template-columns:repeat(3,79px);grid-auto-rows:51px}
  .cell{display:flex;align-items:center;justify-content:center;text-align:center;padding:4px;font-size:4.3px;line-height:1.5;color:#fff}
  .cell.orange{background:var(--orange)}.cell.slate{background:var(--slate)}

  /* closing */
  .thanks{position:absolute;left:0;right:0;top:32px;text-align:center;font-size:25px;font-weight:300;color:#fff}
  .thanks-sub{position:absolute;left:0;right:0;top:66px;text-align:center;font-size:5.5px;font-weight:700;color:#fff}
  .thanks::before,.thanks::after{content:"";position:absolute;top:19px;width:55px;height:1px;background:#fff}
  .thanks::before{left:14px}.thanks::after{right:14px}
  .closing-mark{position:absolute;left:126px;top:132px;width:30px;height:30px;border-radius:50%;background:var(--orange)}
  .closing-name{position:absolute;left:0;right:0;top:179px;text-align:center;font-size:8.5px;color:var(--charcoal)}
</style>
</head>
<body>

<!-- Cover -->
<section class="slide cover" style="left:17px;top:18px">
  <svg class="cover-art" viewBox="0 0 280 210" aria-hidden="true">
    <path d="M0,92 C70,88 160,130 280,92 L280,210 L0,210 Z" fill="var(--orange)"/>
    <path d="M150,112 C200,114 240,102 280,82 L280,96 C230,116 195,120 150,112 Z" fill="var(--charcoal)"/>
  </svg>
  <div class="cover-mark"></div>
  <div class="cover-name">Harbor Ledger Pathfinders</div>
  <h1 class="cover-title">Presentation Title Goes Here</h1>
  <p class="cover-sub">SUBTITLE OF THE PRESENTATION GOES HER</p>
</section>

<!-- Table of contents -->
<section class="slide" style="left:312px;top:18px">
  <h2 class="slide-title">Table of contents</h2><div class="header-rule"></div>
  <div class="brand-dot"></div><div class="brand-name">Harbor Ledger Pathfinders</div>
  <div class="toc-item" style="left:25px;top:50px"><span class="toc-num">1</span>About Us</div>
  <div class="toc-item" style="left:25px;top:76px"><span class="toc-num">2</span>Business</div>
  <div class="toc-item" style="left:25px;top:101px"><span class="toc-num">3</span>Contact Center</div>
  <div class="toc-item" style="left:25px;top:126px"><span class="toc-num">4</span>Communication</div>
  <div class="toc-item" style="left:143px;top:50px"><span class="toc-num">5</span>Consultants</div>
  <div class="toc-item" style="left:143px;top:76px"><span class="toc-num">6</span>Client Testimonials</div>
  <div class="toc-item" style="left:143px;top:101px"><span class="toc-num">7</span>Portfolio</div>
  <div class="toc-item" style="left:143px;top:126px"><span class="toc-num">7</span>Contact Us</div>
  <svg class="wave" viewBox="0 0 280 60" aria-hidden="true"><path d="M0,32 C80,30 150,64 280,24 L280,60 L0,60 Z" fill="var(--orange)"/><path d="M70,38 C150,56 220,42 280,12 L280,24 C210,52 150,56 70,38 Z" fill="var(--charcoal)"/></svg>
  <div class="footer-name">Harbor Ledger<br>Pathfinders</div><div class="page-no">1</div>
</section>

<!-- Who we are -->
<section class="slide" style="left:608px;top:18px">
  <h2 class="slide-title">Who we are</h2><div class="header-rule"></div>
  <div class="brand-dot"></div><div class="brand-name">Harbor Ledger Pathfinders</div>
  <p class="body-copy" style="position:absolute;left:10px;top:44px;width:138px">Lorem Ipsum is simply dummy text of the printing and typesetting industry. Lorem Ipsum has been the industry's standard dummy text ever since the 1500s, when an unknown printer took a galley of type and scrambled it to make a type specimen book. It has survived not only five centuries, but also the leap into electronic typesetting, remaining essentially unchanged. It was popularised in the 1960s with the release of Letraset sheets containing Lorem Ipsum passages.<br><br>Lorem Ipsum has been the industry's standard dummy text ever since the 1500s, when an unknown printer took a galley of type and scrambled.</p>
  <div class="placeholder" role="img" aria-label="Photo of a business team standing in front of a globe" style="left:156px;top:44px;width:112px;height:106px;background:linear-gradient(180deg,#9a9a9a 0%,#2a2a2a 60%,#e6e6e6 100%)"></div>
  <svg class="wave" viewBox="0 0 280 60" aria-hidden="true"><path d="M0,32 C80,30 150,64 280,24 L280,60 L0,60 Z" fill="var(--orange)"/><path d="M70,38 C150,56 220,42 280,12 L280,24 C210,52 150,56 70,38 Z" fill="var(--charcoal)"/></svg>
  <div class="footer-name">Harbor Ledger<br>Pathfinders</div><div class="page-no">2</div>
</section>

<!-- How we are planning -->
<section class="slide" style="left:904px;top:18px">
  <h2 class="slide-title">How we are planning</h2><div class="header-rule"></div>
  <div class="brand-dot"></div><div class="brand-name">Harbor Ledger Pathfinders</div>
  <svg style="position:absolute;left:10px;top:40px" width="262" height="30" viewBox="0 0 262 30" aria-hidden="true">
    <path d="M0,0 H62 L76,15 L62,30 H0 Z" fill="var(--orange)"/>
    <path d="M65,0 H172 L186,15 L172,30 H65 L79,15 Z" fill="var(--charcoal)"/>
    <path d="M175,0 H248 L262,15 L248,30 H175 L189,15 Z" fill="var(--orange)"/>
  </svg>
  <div class="step-label" style="left:8px"><small>Step 1</small><span>Starting</span></div>
  <div class="step-label" style="left:102px"><small>Step 2</small><span>Planning</span></div>
  <div class="step-label" style="left:195px"><small>Step 3</small><span>Complete</span></div>
  <p class="body-copy" style="position:absolute;left:10px;top:86px;width:124px">Lorem Ipsum is simply dummy text of the printing and typesetting industry. Lorem Ipsum has been the industry's standard dummy text ever since the 1500s, when an unknown printer took a galley of type and scrambled it to make a type specimen book. It has survived not only five centuries, but also the leap into electronic typesetting, remaining essentially unchanged.</p>
  <p class="body-copy" style="position:absolute;left:146px;top:86px;width:124px">Lorem Ipsum is simply dummy text of the printing and typesetting industry. Lorem Ipsum has been the industry's standard dummy text ever since the 1500s, when an unknown printer took a galley of type and scrambled it to make.</p>
  <svg class="wave" viewBox="0 0 280 60" aria-hidden="true"><path d="M0,32 C80,30 150,64 280,24 L280,60 L0,60 Z" fill="var(--orange)"/><path d="M70,38 C150,56 220,42 280,12 L280,24 C210,52 150,56 70,38 Z" fill="var(--charcoal)"/></svg>
  <div class="footer-name">Harbor Ledger<br>Pathfinders</div><div class="page-no">3</div>
</section>

<!-- Team -->
<section class="slide" style="left:17px;top:246px">
  <h2 class="slide-title">Our teem</h2><div class="header-rule"></div>
  <div class="brand-dot"></div><div class="brand-name">Harbor Ledger Pathfinders</div>
  <div class="portrait" style="left:27px"><div role="img" aria-label="Team member portrait"></div></div>
  <div class="portrait" style="left:114px"><div role="img" aria-label="Team member portrait"></div></div>
  <div class="portrait" style="left:200px"><div role="img" aria-label="Team member portrait"></div></div>
  <p class="team-copy" style="left:20px">Lorem Ipsum is simply dummy text of the printing and typesetting industry. Lorem Ipsum has been the industry's standard galley</p>
  <p class="team-copy" style="left:107px">Lorem Ipsum is simply dummy text of the printing and typesetting industry. Lorem Ipsum has been the industry's standard galley</p>
  <p class="team-copy" style="left:193px">Lorem Ipsum is simply dummy text of the printing and typesetting industry. Lorem Ipsum has been the industry's standard galley</p>
  <svg class="wave" viewBox="0 0 280 60" aria-hidden="true"><path d="M0,32 C80,30 150,64 280,24 L280,60 L0,60 Z" fill="var(--orange)"/><path d="M70,38 C150,56 220,42 280,12 L280,24 C210,52 150,56 70,38 Z" fill="var(--charcoal)"/></svg>
  <div class="footer-name">Harbor Ledger<br>Pathfinders</div><div class="page-no">4</div>
</section>

<!-- Video -->
<section class="slide" style="left:312px;top:246px">
  <h2 class="slide-title">Video with description</h2><div class="header-rule"></div>
  <div class="brand-dot"></div><div class="brand-name">Harbor Ledger Pathfinders</div>
  <div class="placeholder" role="img" aria-label="Embedded video player with still frame" style="left:8px;top:45px;width:141px;height:103px;background:linear-gradient(180deg,#6b5a4c 0%,#3a3029 75%,#111 100%);border:2px solid #222"></div>
  <div class="callout" style="left:151px;top:58px;width:120px;height:85px">Lorem Ipsum is simply dummy text of the printing and typesetting industry. Lorem Ipsum has been the industry's standard dummy text ever since the 1500s, when an unknown printer took a galley of type and scrambled it to make a type specimen book. It has survived not only five centuries, but also the leap into electronic typesetting, remaining essentially unchanged.</div>
  <svg class="wave" viewBox="0 0 280 60" aria-hidden="true"><path d="M0,32 C80,30 150,64 280,24 L280,60 L0,60 Z" fill="var(--orange)"/><path d="M70,38 C150,56 220,42 280,12 L280,24 C210,52 150,56 70,38 Z" fill="var(--charcoal)"/></svg>
  <div class="footer-name">Harbor Ledger<br>Pathfinders</div><div class="page-no">5</div>
</section>

<!-- Investors -->
<section class="slide" style="left:608px;top:246px">
  <h2 class="slide-title">Investors</h2><div class="header-rule"></div>
  <div class="brand-dot"></div><div class="brand-name">Harbor Ledger Pathfinders</div>
  <svg style="position:absolute;left:0;top:0" width="280" height="210" viewBox="0 0 280 210" role="img" aria-label="Pie chart: Industrial 59%, Investors 23%, Financial 17%">
    <path d="M142,99 L142,54 A45,45 0 1 1 117.9,137 Z" fill="var(--pie-blue)"/>
    <path d="M142,99 L117.9,137 A45,45 0 0 1 101.3,79.8 Z" fill="var(--pie-red)"/>
    <path d="M142,99 L101.3,79.8 A45,45 0 0 1 142,54 Z" fill="var(--pie-green)"/>
    <g fill="#fff" font-size="6.5" font-family="Open Sans, sans-serif" text-anchor="middle">
      <text x="164" y="111">59%</text><text x="113" y="115">23%</text><text x="126" y="83">17%</text>
    </g>
    <g stroke="#a9b9cc" stroke-width=".6" fill="none">
      <polyline points="44,52 90,52 120,64"/><polyline points="186,52 222,52"/><polyline points="44,136 70,136 110,122"/>
    </g>
  </svg>
  <div class="chart-label" style="left:10px;top:44px">Financial</div>
  <p class="body-copy" style="position:absolute;left:10px;top:55px;width:50px">Lorem Ipsum is simply dummy text of the printing and typesetting industry. Lorem Ipsum has been the industry's standard galley</p>
  <div class="chart-label" style="left:225px;top:44px">Industrial</div>
  <p class="body-copy" style="position:absolute;left:225px;top:55px;width:46px">Lorem Ipsum is simply dummy text of the printing and typesetting industry. Lorem Ipsum has been the industry's standard galley</p>
  <div class="chart-label" style="left:10px;top:131px">Investors</div>
  <p class="body-copy" style="position:absolute;left:10px;top:142px;width:100px">Lorem Ipsum is simply dummy text of the printing and typesetting industry. Lorem Ipsum has been the industry's standard galley</p>
  <svg class="wave" viewBox="0 0 280 60" aria-hidden="true"><path d="M0,32 C80,30 150,64 280,24 L280,60 L0,60 Z" fill="var(--orange)"/><path d="M70,38 C150,56 220,42 280,12 L280,24 C210,52 150,56 70,38 Z" fill="var(--charcoal)"/></svg>
  <div class="footer-name">Harbor Ledger<br>Pathfinders</div><div class="page-no">6</div>
</section>

<!-- Graph -->
<section class="slide" style="left:904px;top:246px">
  <h2 class="slide-title">Graph</h2><div class="header-rule"></div>
  <div class="brand-dot"></div><div class="brand-name">Harbor Ledger Pathfinders</div>
  <svg style="position:absolute;left:0;top:0" width="280" height="210" viewBox="0 0 280 210" role="img" aria-label="Bar chart of five categories rising from 2 to 10">
    <g font-size="5.5" fill="#555" font-family="Open Sans, sans-serif" text-anchor="end">
      <text x="40" y="147">0</text><text x="40" y="131">2</text><text x="40" y="115">4</text><text x="40" y="99">6</text><text x="40" y="83">8</text><text x="40" y="67">10</text><text x="40" y="51">12</text>
    </g>
    <line x1="45" y1="145" x2="248" y2="145" stroke="#bbb" stroke-width=".7"/>
    <rect x="53" y="129" width="8" height="16" fill="var(--pie-blue)"/>
    <rect x="93" y="113" width="8" height="32" fill="var(--pie-green)"/>
    <rect x="133" y="97" width="8" height="48" fill="var(--charcoal)"/>
    <rect x="173" y="81" width="8" height="64" fill="var(--bar-cyan)"/>
    <rect x="213" y="65" width="8" height="80" fill="var(--orange)"/>
    <g font-size="5.5" fill="#555" font-family="Open Sans, sans-serif" text-anchor="middle">
      <text x="57" y="155">Category 1</text><text x="97" y="155">Category 2</text><text x="137" y="155">Category 3</text><text x="177" y="155">Category 4</text><text x="217" y="155">Category 4</text>
    </g>
  </svg>
  <svg class="wave" viewBox="0 0 280 60" aria-hidden="true"><path d="M0,32 C80,30 150,64 280,24 L280,60 L0,60 Z" fill="var(--orange)"/><path d="M70,38 C150,56 220,42 280,12 L280,24 C210,52 150,56 70,38 Z" fill="var(--charcoal)"/></svg>
  <div class="footer-name">Harbor Ledger<br>Pathfinders</div><div class="page-no">7</div>
</section>

<!-- Investment highlights -->
<section class="slide" style="left:312px;top:473px">
  <h2 class="slide-title">Investment Highlights</h2><div class="header-rule"></div>
  <div class="brand-dot"></div><div class="brand-name">Harbor Ledger Pathfinders</div>
  <div class="highlight-grid">
    <div class="cell orange">Lorem Ipsum is simply dummy text of the printing and typesetting industry. Lorem Ipsum has been the industry's standard galley</div>
    <div class="cell slate">Lorem Ipsum is simply dummy text of the printing and typesetting industry. Lorem Ipsum has been the industry's standard galley</div>
    <div class="cell orange">Lorem Ipsum is simply dummy text of the printing and typesetting industry. Lorem Ipsum has been the industry's standard galley</div>
    <div class="cell slate">Lorem Ipsum is simply dummy text of the printing and typesetting industry. Lorem Ipsum has been the industry's standard galley</div>
    <div class="cell orange">Lorem Ipsum is simply dummy text of the printing and typesetting industry. Lorem Ipsum has been the industry's standard galley</div>
  </div>
  <svg class="wave" viewBox="0 0 280 60" aria-hidden="true"><path d="M0,32 C80,30 150,64 280,24 L280,60 L0,60 Z" fill="var(--orange)"/><path d="M70,38 C150,56 220,42 280,12 L280,24 C210,52 150,56 70,38 Z" fill="var(--charcoal)"/></svg>
  <div class="footer-name">Harbor Ledger<br>Pathfinders</div><div class="page-no">8</div>
</section>

<!-- Back cover -->
<section class="slide closing" style="left:608px;top:473px">
  <svg class="closing-art" viewBox="0 0 280 210" aria-hidden="true">
    <path d="M0,0 H280 V72 C200,104 110,104 0,76 Z" fill="var(--orange)"/>
    <path d="M60,92 C140,110 210,104 280,74 L280,84 C210,114 140,118 60,92 Z" fill="var(--charcoal)"/>
  </svg>
  <h2 class="thanks">Thank You</h2>
  <p class="thanks-sub">Thanks for your feedback</p>
  <div class="closing-mark"></div>
  <div class="closing-name">Harbor Ledger Pathfinders</div>
</section>

</body>
</html>
```